Safety training business card design

We need a buisness card design and logo for a small buisness that provides safety training through out the mining and civil construction industries. We provide first aid , confined space working at heights , machinery tickets, chainsaw, four wheel drive and four wheel motorbike training. We would like to use the design colors of navy blue, Fluro or lime green and white .

Industry/Entity Type

Construction

Contact Information for Business Card

Kelbrook Earthmoving & Training , Dennis Holloway, kelbrook.training@mailbox-example.com, ph 0438615044 abn 47 816 305 971

```html
<!DOCTYPE html>
<html lang="en">
<head>
<meta charset="utf-8">
<title>Kelbrook Earthmoving &amp; Training – Business Card</title>
<link rel="stylesheet" href="https://fonts.googleapis.com/css2?family=Source+Sans+3:wght@400;700&display=swap">
<style>
  :root {
    --navy: #1f2a5a;
    --lime: #8dc63f;
    --card-bg: #f7f7f7;
    --page-bg: #ffffff;
    --frame: #2a3463;
  }
  html, body {
    margin: 0;
    padding: 0;
    width: 1200px;
    height: 372px;
    overflow: hidden;
    background: var(--page-bg);
    font-family: "Source Sans 3", sans-serif;
  }
  .canvas {
    position: relative;
    width: 1200px;
    height: 372px;
  }
  .card {
    position: absolute;
    top: 5px;
    height: 361px;
    background: var(--card-bg);
    border: 2px solid var(--frame);
    box-sizing: border-box;
    overflow: hidden;
  }
  .card--front { left: 11px; width: 585px; }
  .card--back  { left: 607px; width: 583px; }

  .stripe {
    position: absolute;
    width: 20px;
  }
  .stripe--navy { background: var(--navy); }
  .stripe--lime { background: var(--lime); }

  .card--front .stripe--navy.stripe--upper { left: 494px; top: 5px; height: 233px; }
  .card--front .stripe--lime.stripe--upper { left: 526px; top: 5px; height: 233px; }
  .card--front .stripe--navy.stripe--lower { left: 494px; top: 264px; height: 95px; }
  .card--front .stripe--lime.stripe--lower { left: 526px; top: 264px; height: 95px; }

  .card--back .stripe--navy { left: 495px; top: 3px; height: 355px; }
  .card--back .stripe--lime { left: 528px; top: 3px; height: 355px; }

  .brand {
    position: absolute;
    display: flex;
    align-items: center;
    color: var(--navy);
    font-weight: 700;
    line-height: 1;
    white-space: nowrap;
  }
  .brand__square {
    background: var(--navy);
    flex: none;
  }
  .card--front .brand { left: 36px; top: 118px; gap: 14px; font-size: 46px; }
  .card--front .brand__square { width: 46px; height: 46px; }
  .card--back .brand { left: 60px; top: 190px; gap: 18px; font-size: 60px; }
  .card--back .brand__square { width: 60px; height: 60px; }

  .contact {
    position: absolute;
    left: 36px;
    top: 224px;
    margin: 0;
    color: var(--navy);
    font-size: 21px;
    line-height: 28px;
    font-weight: 400;
    font-style: normal;
  }
  .contact span { display: block; white-space: nowrap; }
</style>
</head>
<body>
<div class="canvas">
  <section class="card card--front">
    <div class="brand">
      <span class="brand__square"></span>
      <span class="brand__name">KELBROOK</span>
    </div>
    <address class="contact">
      <span>Kelbrook Earthmoving &amp; Training , Dennis Holloway,</span>
      <span>kelbrook.training@mailbox-example.com,</span>
      <span>ph 0438615044 abn 47 816 305 971</span>
    </address>
    <div class="stripe stripe--navy stripe--upper"></div>
    <div class="stripe stripe--lime stripe--upper"></div>
    <div class="stripe stripe--navy stripe--lower"></div>
    <div class="stripe stripe--lime stripe--lower"></div>
  </section>

  <section class="card card--back">
    <div class="brand">
      <span class="brand__square"></span>
      <span class="brand__name">KELBROOK</span>
    </div>
    <div class="stripe stripe--navy"></div>
    <div class="stripe stripe--lime"></div>
  </section>
</div>
</body>
</html>
```